Grins of Maplecrest - Dental, needs a redesign

Purpose:
Redesign website: http://www.grinsofmaplecrest.example/

Sections are important, but for content, we can use existing website or have some placeholder text to fill in later.

Some of the required sections:
About us, contact us, services, our offices, our staff, patient education, patient forms (link to Molvaro can be used here), link to friendwall, testimonials

Editability:
We would like to be able to update and edit the content in the future, for small changes

Pictures:
Here is a link to the staff pictures we’d like to use on the website:
https://www.filecrate.example/sh/503k7pq2vv884x9/BBDPyrTe_wKQj7ZumfXKTgghb?dl=0
You don't have to use all the pictures; just a few.

Friendwall page:
https://www.friendwall.example/Grins-of-Maplecrest-527163048915276

Colors: Calming colors/images for a soothing feeling... to assure the patient that it'll not be that bad.

Target Market(s)

General population

Industry/Entity Type

Dental Clinic

Coding

Coded - Design and coding required

Number of Pages Required

5+ page

Requirements
Must have
• About us, contact us, services, our offices, our staff, patient education, patient forms (link to Molvaro can be used here), link to friendwall, testimonials.
• Just create the placeholders for content or use from existing website.
• The staff picture of everyone needs to be on the home page - because that makes it more personal and has received positive feedback from many patients.

```html
<!DOCTYPE html>
<html lang="en">
<head>
<meta charset="utf-8">
<title>Grins of Maplecrest - Dental</title>
<link href="https://fonts.googleapis.com/css2?family=Lato:ital,wght@0,400;0,700;0,900;1,900&display=swap" rel="stylesheet">
<style>
:root{
  --teal:#3fc3c8;
  --teal-deep:#2aa9b0;
  --teal-dark:#1f7f86;
  --purple:#a57ee6;
  --purple-soft:#b897ee;
  --ink:#333;
  --muted:#666;
  --light:#f1f1f1;
  --footer:#262626;
  --footer-bar:#1a1a1a;
  --white:#fff;
}
*{box-sizing:border-box;margin:0;padding:0}
html,body{width:1200px;height:3046px;overflow:hidden}
body{font-family:'Lato',sans-serif;color:var(--ink);background:var(--white);position:relative}
section,header,footer{position:absolute;left:0;width:1200px}

/* top bar + header */
.topbar{top:0;height:40px;left:620px;width:580px;background:var(--teal);color:var(--white);font-size:15px;font-weight:700;display:flex;align-items:center;gap:34px;padding-left:40px;z-index:2}
.topbar .item{display:flex;align-items:center;gap:8px}
.topbar .dot{width:22px;height:22px;border-radius:50%;background:var(--white);margin-left:6px}
.site-header{top:40px;height:96px;background:var(--white);box-shadow:0 2px 4px rgba(0,0,0,.08)}
.brand{position:absolute;left:116px;top:20px;font-size:30px;font-weight:900;color:var(--purple);line-height:1;text-transform:uppercase;display:flex;align-items:center;gap:12px}
.brand .mark{width:40px;height:40px;border-radius:50%;background:var(--teal)}
.brand small{display:block;font-size:30px}
.nav{position:absolute;left:520px;top:38px;display:flex;font-size:14px}
.nav a{color:var(--ink);text-decoration:none;padding:0 16px;border-left:1px solid #ddd}
.nav a:first-child{border-left:0;color:var(--purple);text-decoration:underline}

/* hero */
.hero{top:136px;height:514px;background:
  radial-gradient(ellipse 300px 220px at 150px 300px,#8fd0ee 0%,rgba(143,208,238,0) 100%),
  radial-gradient(ellipse 420px 300px at 780px 220px,#f0cdb8 0%,rgba(240,205,184,0) 100%),
  linear-gradient(100deg,#d7ebf6 0%,#ecdcd2 40%,#efd4c2 70%,#d8bcab 100%)}
.hero .band{position:absolute;left:0;bottom:0;width:100%;height:86px;background:rgba(30,30,30,.72)}
.hero h1{position:absolute;left:100px;bottom:24px;color:var(--white);font-style:italic;font-weight:900;font-size:34px}
.hero .cta{position:absolute;left:802px;bottom:16px;background:var(--teal);color:var(--white);font-weight:700;font-size:18px;padding:10px 22px 10px 14px;border-radius:3px;display:flex;align-items:center;gap:14px;text-transform:uppercase}
.hero .cta .cal{width:34px;height:30px;border:2px solid var(--white);border-radius:3px}
.arrow{position:absolute;top:220px;color:var(--white);font-size:40px}

/* section headings */
.heading{position:absolute;left:0;width:100%;text-align:center;font-weight:700;text-transform:uppercase;font-size:31px}
.divider{position:absolute;left:50%;width:240px;margin-left:-120px;height:1px;background:currentColor;opacity:.4}
.divider::after{content:"";position:absolute;left:50%;top:-7px;margin-left:-7px;width:14px;height:14px;border-radius:50%;background:inherit}

/* welcome */
.welcome{top:650px;height:330px}
.welcome .heading{top:40px;color:var(--purple)}
.welcome .heading span{color:var(--teal)}
.welcome .divider{top:88px;color:var(--purple)}
.welcome p{position:absolute;left:122px;width:956px;top:114px;text-align:center;font-size:13px;line-height:27px;color:var(--ink)}
.btn{background:var(--teal);color:var(--white);font-weight:700;font-size:13px;text-transform:uppercase;border-radius:3px;text-align:center}
.welcome .btn{position:absolute;left:548px;top:246px;width:104px;height:36px;line-height:36px}

/* services */
.services{top:980px;height:528px;background:linear-gradient(180deg,#48c6cb 0%,#3ebfc4 55%,#52ccd0 100%);color:var(--white)}
.services .heading{top:40px}
.services .divider{top:90px;color:var(--white)}
.svc{position:absolute;width:240px}
.svc h3{font-size:20px;font-weight:700;margin-bottom:6px}
.svc p{font-size:13px;line-height:17px;color:#e3f7f8}
.svc.left{text-align:right}
.icon-box{position:absolute;width:96px;height:94px;border:2px solid var(--teal-dark);border-radius:4px;background:rgba(255,255,255,.08)}
.center-mark{position:absolute;left:507px;top:170px;width:193px;height:262px;display:flex;align-items:center;justify-content:center;text-align:center;font-size:24px;font-weight:900;text-transform:uppercase;line-height:1.2}

/* team */
.team{top:1508px;height:432px;background:var(--light)}
.team .heading{top:30px;color:var(--teal)}
.team .divider{top:80px;color:var(--purple)}
.cards{position:absolute;left:97px;top:144px;display:flex;gap:7px}
.card{width:195px;height:232px;background:var(--white)}
.card .photo{height:130px;background:linear-gradient(180deg,#b46f5c 0%,#9a6152 50%,#2f2a2c 100%)}
.card:nth-child(2) .photo{background:linear-gradient(180deg,#4f6f80 0%,#7e6a5e 55%,#2c2a2c 100%)}
.card:nth-child(5) .photo{background:linear-gradient(180deg,#a89388 0%,#8a7466 55%,#333 100%)}
.card h4{color:var(--teal);font-size:14px;font-weight:700;padding:12px 12px 4px}
.card p{font-size:12.5px;line-height:18px;color:var(--muted);padding:0 12px}
.card p span{color:var(--teal)}

/* hours + testimonials */
.split{top:1940px;height:450px}
.hours{position:absolute;left:0;top:0;width:600px;height:450px;background:linear-gradient(135deg,#6fd0d4 0%,#4cc3c8 50%,#63ccd0 100%);color:var(--white)}
.hours .heading,.testi .heading{top:30px}
.hours .divider,.testi .divider{top:80px;color:var(--white)}
.hours table{position:absolute;left:142px;top:130px;width:410px;border-collapse:collapse;font-weight:700}
.hours td{height:45px;font-size:14px}
.hours tr:nth-child(odd) td{background:rgba(255,255,255,.15)}
.hours td.day{text-align:right;width:150px;padding-right:14px}
.hours td.sep{width:20px;text-align:center}
.hours td.time{font-size:17px;padding-left:10px}
.hours td small{display:block;font-size:14px;line-height:1.1}
.testi{position:absolute;left:600px;top:0;width:600px;height:450px;background:linear-gradient(135deg,#b999ee 0%,#a47fe6 50%,#b290ec 100%);color:var(--white)}
.portraits{position:absolute;left:0;top:150px;width:600px;height:112px}
.portraits div{position:absolute;border-radius:50%;border:3px solid var(--white)}
.testi .name{position:absolute;left:142px;width:200px;top:280px;text-align:center;font-size:22px;font-weight:900;color:#2a1f45}
.testi p{position:absolute;left:64px;width:460px;top:330px;text-align:center;font-size:12.5px;line-height:21px}
.testi .arr{position:absolute;top:180px;font-size:36px}

/* appointment */
.appointment{top:2390px;height:290px}
.appointment h2{position:absolute;left:100px;top:46px;color:var(--teal);font-size:37px;font-weight:700;line-height:46px;text-transform:uppercase}
.appointment .intro{position:absolute;left:100px;top:158px;width:320px;font-size:13px;line-height:21px;color:var(--muted)}
.appointment .note{position:absolute;left:459px;top:50px;font-size:13px;color:var(--muted)}
.field{position:absolute;height:44px;border:1px solid #ccc;font-size:13px;color:var(--muted);padding:14px 12px}
.appointment .btn{position:absolute;left:459px;top:188px;width:86px;height:40px;line-height:40px;font-size:15px;font-weight:400}

/* footer */
.site-footer{top:2620px;height:426px}
.site-footer .wave{position:absolute;left:0;top:0}
.footer-body{position:absolute;left:0;top:130px;width:1200px;height:255px;background:var(--footer);color:#ddd}
.col{position:absolute;top:55px;font-size:13px;line-height:23px}
.col h5{color:var(--teal);font-size:17px;font-weight:700;margin-bottom:8px;border-bottom:1px solid #555;padding-bottom:2px;display:inline-block}
.col ul{list-style:none}
.col li::before{content:"› ";color:#888}
.ci{display:flex;gap:10px;align-items:flex-start}
.ci svg{margin-top:6px;flex:none}
.newsletter p{line-height:19px}
.newsletter .email{width:190px;height:30px;background:var(--white);color:var(--muted);font-size:12px;padding:4px 10px;margin-top:14px}
.newsletter .btn{width:90px;height:30px;line-height:30px;margin-top:12px;text-transform:none;font-size:13px}
.footer-brand{position:absolute;left:938px;top:130px;color:var(--teal-deep);font-size:32px;font-weight:900;text-transform:uppercase;line-height:34px}
.copy{position:absolute;left:0;top:385px;width:1200px;height:41px;background:var(--footer-bar);color:#ddd;font-size:13px;display:flex;align-items:center;justify-content:space-between;padding:0 120px}
.copy .follow{display:flex;align-items:center;gap:10px;font-weight:700}
.copy .follow span.dot{width:26px;height:26px;border-radius:50%;border:2px solid #ddd}
</style>
</head>
<body>

<div class="topbar">
  <div class="item"><svg width="16" height="16" viewBox="0 0 24 24"><path fill="#fff" d="M6.6 10.8a15.1 15.1 0 006.6 6.6l2.2-2.2c.3-.3.7-.4 1-.2 1.1.4 2.3.6 3.6.6.6 0 1 .4 1 1V20c0 .6-.4 1-1 1A17 17 0 013 4c0-.6.4-1 1-1h3.5c.6 0 1 .4 1 1 0 1.3.2 2.5.6 3.6.1.3 0 .7-.2 1z"/></svg>555-210-4418</div>
  <div class="item"><svg width="16" height="16" viewBox="0 0 24 24"><rect x="2" y="5" width="20" height="14" rx="2" fill="#fff"/><path d="M3 6l9 7 9-7" stroke="#3fc3c8" stroke-width="2" fill="none"/></svg>info@grinsofmaplecrest.example</div>
  <span class="dot" aria-label="Friendwall"></span>
</div>

<header class="site-header">
  <div class="brand"><span class="mark"></span><span>Grins<small>of Maplecrest</small></span></div>
  <nav class="nav">
    <a>Home</a><a>About us</a><a>Services</a><a>Our Staff</a><a>Testimonials</a><a>Our offices</a><a>Contact us</a>
  </nav>
</header>

<section class="hero" role="img" aria-label="Photo of a dentist in blue gloves examining a smiling patient's teeth">
  <span class="arrow" style="left:14px">‹</span>
  <span class="arrow" style="right:14px">›</span>
  <div class="band">
    <h1>Honestly Caring &amp; Quality Dentistry</h1>
    <div class="cta"><span class="cal"></span>Make an appointment</div>
  </div>
</section>

<section class="welcome">
  <h2 class="heading">Welcome to <span>Grins of Maplecrest</span></h2>
  <div class="divider"></div>
  <p>Dr. Priya Venkat provides a full range of dental services to the whole family. Many of our patient families span multiple generations. Our Team are dedicated to taking the time needed to provide the very best care every patient deserves. Please tour our web site to learn more about family dentistry, cosmetic dentistry and our restorative dental services. We invite you to call us with any questions you may have - we all look forward to meeting you and your family! New patients looking for quality dental care in a relaxed environment are welcome! We accept PPO, Indeminity and Traditional Insurance plans.</p>
  <div class="btn">Read more</div>
</section>

<section class="services">
  <h2 class="heading">Our Services</h2>
  <div class="divider"></div>

  <div class="svc left" style="left:118px;top:182px"><h3>General Dental Health</h3><p>Ut wisi enim ad minim veniam, quismpi [+].... nostrud exerci tation ullamco</p></div>
  <div class="icon-box" style="left:376px;top:170px"><svg width="96" height="94" viewBox="0 0 96 94"><g stroke="#fff" stroke-width="3" fill="none"><path d="M34 26v40M30 66h8M62 26v40M58 66h8"/><circle cx="34" cy="24" r="5"/><path d="M62 20l6 6"/></g></svg></div>

  <div class="svc left" style="left:118px;top:348px"><h3>Dental FAQ</h3><p>Ut wisi enim ad minim veniam, quismpi [+].... nostrud exerci tation ullamco</p></div>
  <div class="icon-box" style="left:376px;top:336px"><svg width="96" height="94" viewBox="0 0 96 94"><g stroke="#fff" stroke-width="3" fill="none"><circle cx="48" cy="34" r="11"/><path d="M26 72c0-12 10-20 22-20s22 8 22 20"/></g></svg></div>

  <div class="center-mark">Grins of<br>Maplecrest</div>

  <div class="icon-box" style="left:727px;top:170px"><svg width="96" height="94" viewBox="0 0 96 94"><g stroke="#fff" stroke-width="3" fill="none"><path d="M22 40c8 18 44 18 52 0z"/><path d="M30 42h36"/></g></svg></div>
  <div class="svc" style="left:842px;top:182px"><h3>Cosmetic Dentistry</h3><p>Ut wisi enim ad minim veniam, quismpi nostrud exerci tation ullamco ....[+]</p></div>

  <div class="icon-box" style="left:727px;top:336px"><svg width="96" height="94" viewBox="0 0 96 94"><g stroke="#fff" stroke-width="3" fill="none"><path d="M28 64h40M34 64l8-18h22M42 46l-6-16M36 72v-8M62 72v-8"/></g></svg></div>
  <div class="svc" style="left:842px;top:348px"><h3>Advanced Procedures</h3><p>Ut wisi enim ad minim veniam, quismpi nostrud exerci tation ullamco ....[+]</p></div>
</section>

<section class="team">
  <h2 class="heading">Our Team</h2>
  <div class="divider"></div>
  <div class="cards">
    <div class="card"><div class="photo" role="img" aria-label="Staff photo of Dr. Priya Venkat in front of a brick wall"></div><h4>Dr. Priya Venkat</h4><p>Duis autem vel eum iriure dolormi opl inmoki hendi rerit vulpu tatemi velitm <span>[+]</span></p></div>
    <div class="card"><div class="photo" role="img" aria-label="Staff photo of a team member in the office"></div><h4>Lorem ipsum</h4><p>Duis autem vel eum iriure dolormi opl inmoki hendi rerit vulpu tatemi velitm <span>[+]</span></p></div>
    <div class="card"><div class="photo" role="img" aria-label="Staff photo of a team member in front of a brick wall"></div><h4>Lorem ipsum</h4><p>Duis autem vel eum iriure dolormi opl inmoki hendi rerit vulpu tatemi velitm <span>[+]</span></p></div>
    <div class="card"><div class="photo" role="img" aria-label="Staff photo of a team member in front of a brick wall"></div><h4>Lorem ipsum</h4><p>Duis autem vel eum iriure dolormi opl inmoki hendi rerit vulpu tatemi velitm <span>[+]</span></p></div>
    <div class="card"><div class="photo" role="img" aria-label="Staff photo of a team member in a stone-walled room"></div><h4>Lorem ipsum</h4><p>Duis autem vel eum iriure dolormi opl inmoki hendi rerit vulpu tatemi velitm <span>[+]</span></p></div>
  </div>
</section>

<section class="split">
  <div class="hours" role="img" aria-label="Softly blurred clinic interior behind the opening hours">
    <h2 class="heading">Opening Hours</h2>
    <div class="divider"></div>
    <table>
      <tr><td class="day">Monday</td><td class="sep">:</td><td class="time">12:00pm to 6:00pm</td></tr>
      <tr><td class="day">Tuesday</td><td class="sep">:</td><td class="time">10:00am to 7:00pm</td></tr>
      <tr><td class="day">Wednesday</td><td class="sep">:</td><td class="time">Closed</td></tr>
      <tr><td class="day">Friday</td><td class="sep">:</td><td class="time">8:00am to 6:00pm</td></tr>
      <tr><td class="day">Saturday<small>when open</small></td><td class="sep">:</td><td class="time">8:00am to 3:00pm OR<br>8:00am to 12:00pm</td></tr>
    </table>
  </div>
  <div class="testi">
    <h2 class="heading">Testimonials</h2>
    <div class="divider"></div>
    <span class="arr" style="left:36px">‹</span>
    <span class="arr" style="right:36px">›</span>
    <div class="portraits" role="img" aria-label="Row of patient portrait photos, the centre one enlarged">
      <div style="left:90px;top:30px;width:52px;height:52px;background:linear-gradient(180deg,#c9b8e2,#a995c8)"></div>
      <div style="left:346px;top:28px;width:58px;height:58px;background:linear-gradient(180deg,#c9b8e2,#a995c8)"></div>
      <div style="left:131px;top:20px;width:72px;height:72px;background:linear-gradient(180deg,#ddd2ec,#b9a7d6)"></div>
      <div style="left:287px;top:22px;width:68px;height:68px;background:linear-gradient(180deg,#e6dbef,#c0aed9)"></div>
      <div style="left:190px;top:0;width:104px;height:104px;background:linear-gradient(180deg,#8f88a6,#55506a)"></div>
    </div>
    <div class="name">-John Doe</div>
    <p>Ut wisi enim adi minim veniam, quis nostrudk exerci tation more ullamcorper suscipit lobortis nis ut aliquip commodo consequt. quis nostrudk Ut wisi enim aliquip adi minim veniam</p>
  </div>
</section>

<section class="appointment">
  <h2>Make an<br>Appointment</h2>
  <p class="intro">Duis autem vel eum iriure dolormi opl inmoki hendi rerit in vulpu tatemi velitm essemol mo molestiel consequ uat, velmi illum dolor eokf no atn nulla more facilisis</p>
  <p class="note">Please fill up bellow form</p>
  <div class="field" style="left:459px;top:82px;width:308px">Name</div>
  <div class="field" style="left:784px;top:82px;width:317px">Email</div>
  <div class="field" style="left:459px;top:134px;width:308px">Phone</div>
  <div class="field" style="left:784px;top:134px;width:317px">Message</div>
  <div class="btn">SUBMIT</div>
</section>

<footer class="site-footer">
  <svg class="wave" width="1200" height="140" viewBox="0 0 1200 140">
    <path d="M0 20 C200 110 500 130 1200 60 L1200 140 L0 140Z" fill="var(--teal-deep)"/>
    <path d="M0 40 C250 125 600 125 1200 72 L1200 140 L0 140Z" fill="var(--footer)"/>
  </svg>
  <div class="footer-body">
    <div class="col" style="left:122px"><h5>Quick Links</h5>
      <ul><li>Home</li><li>About Us</li><li>Services</li><li>Our Staff</li><li>Testimonials</li><li>Our offices</li><li>Contact us</li></ul></div>
    <div class="col" style="left:317px"><h5>Contact Details</h5>
      <div class="ci"><svg width="12" height="14" viewBox="0 0 24 28"><path fill="#3fc3c8" d="M12 0a10 10 0 00-10 10c0 8 10 18 10 18s10-10 10-18A10 10 0 0012 0zm0 14a4 4 0 110-8 4 4 0 010 8z"/></svg><span>418 Alder Row,<br>Suite 2C Maplecrest,<br>IL 60990</span></div>
      <div class="ci" style="margin-top:6px"><svg width="12" height="12" viewBox="0 0 24 24"><path fill="#3fc3c8" d="M6.6 10.8a15.1 15.1 0 006.6 6.6l2.2-2.2c.3-.3.7-.4 1-.2 1.1.4 2.3.6 3.6.6.6 0 1 .4 1 1V20c0 .6-.4 1-1 1A17 17 0 013 4c0-.6.4-1 1-1h3.5c.6 0 1 .4 1 1 0 1.3.2 2.5.6 3.6.1.3 0 .7-.2 1z"/></svg><span>555-210-4418<br>555-210-4419</span></div>
      <div class="ci" style="margin-top:6px"><svg width="12" height="10" viewBox="0 0 24 18"><rect width="24" height="18" rx="2" fill="#3fc3c8"/></svg><span>info@grinsofmaplecrest.example</span></div></div>
    <div class="col newsletter" style="left:599px;width:220px"><h5>Newsletter Sign Up</h5>
      <p>Ut wisi enim ad minim veniam nk quis nostrud exerci tationmo ullm amcorper suscipit lobortis nisl.</p>
      <div class="email">Email Address</div>
      <div class="btn">Subscribe</div></div>
    <div class="footer-brand">Grins of<br>Maplecrest</div>
  </div>
  <div class="copy">
    <span>Copyright © 2016 GRINS OF MAPLECREST. All Right Reserved.</span>
    <span class="follow">Follow Us On <span class="dot" aria-label="Friendwall"></span></span>
  </div>
</footer>

</body>
</html>
```